TRIVEX-PRO Web Design

We are a Health, Safety, Environmental & Quality Recruitment Agency, our clients are major corporate Mining, Oil & Gas and Engineering companies. We have offices in Perth & Melbourne, Australia

The website should be very functional & easy to navigate

BUT REALLY LOOKING FOR WOW FACTOR!
Updates

Please Note: TRIVEX HOLDINGS IS OUR OLD COMPANY THE NEW ONE IS "TRIVEX-PRO" 

Some idea's from our competitors:

http://www.guardlinemerit.com.au/
http://www.wardenplacement.com.au/
http://www.keelhunt.com.au/
http://www.brqstaffing.co.uk/
http://www.laborvane.com/health-safety-environment-jobs

Would love to see some of our valued clients and there logos

still looking for wow factor

Industry/Entity Type

Mining

Requirements
Must have
• A place where candidates can upload there resumes & other contact details
• eg: http://www.guardlinemerit.com.au/candidates/register-your-resume/
• A place we can load jobs on to eg: http://www.guardlinemerit.com.au/vacancies/
• Contact details:
• Perth: 17 Brindlecombe Ave, West Perth, Western Australia 6005
• t: 08 9517 3064 | f: 08 9517 3070 |
• Melbourne: Level 1, 212 Harrowgate Street, Melbourne, Victoria 3000
• t: 03 9655 4217| f: 03 9655 4290 |
• e: dmorl@trivexpro.com.au | w: http://www.trivexpro.com.au

```html
<!DOCTYPE html>
<html lang="en">
<head>
<meta charset="utf-8">
<title>TRIVEX-PRO | Health, Safety, Environment &amp; Quality Recruitment</title>
<link rel="stylesheet" href="https://fonts.googleapis.com/css2?family=Roboto:wght@300;400;500&family=PT+Sans:wght@400;700&display=swap">
<style>
:root{
  --blue:#4b9ccb;
  --blue-band:#5ba3cf;
  --dark:#262223;
  --light:#ececec;
  --text:#333333;
  --muted:#555555;
  --white:#ffffff;
  --grey-text:#cfcfcf;
}
*{margin:0;padding:0;box-sizing:border-box}
html,body{width:894px;height:1200px;overflow:hidden}
body{position:relative;background:var(--white);font-family:Arial,Helvetica,sans-serif;color:var(--text)}
.abs{position:absolute}

/* header */
.site-header{position:absolute;left:0;top:0;width:894px;height:84px;background:var(--white)}
.brand{left:114px;top:22px;display:flex;align-items:center;gap:10px}
.brand-mark{width:38px;height:38px;background:var(--blue)}
.brand-name{font-family:'Roboto',sans-serif;font-weight:300;font-size:30px;color:#555;letter-spacing:1px}
.office-top{left:596px;top:6px;font-family:'PT Sans',sans-serif;font-size:8px;line-height:10px;color:#222}
.office-top h4{font-weight:400;font-size:12px;color:var(--blue);line-height:13px}
.office-top a{color:var(--blue);text-decoration:none}
.main-nav{left:400px;top:62px;display:flex;gap:0}
.main-nav a{font-family:'PT Sans',sans-serif;font-size:10.5px;color:#444;text-decoration:none;padding:2px 9.5px 14px;position:relative}
.main-nav a.active{color:var(--blue)}
.main-nav a.active::after{content:"";position:absolute;left:0;right:0;bottom:0;height:3px;background:var(--blue)}

/* hero */
.hero{left:0;top:84px;width:894px;height:342px;background:
 radial-gradient(ellipse at 70% 95%,rgba(230,170,40,.55),transparent 45%),
 radial-gradient(ellipse at 40% 90%,rgba(120,200,60,.35),transparent 35%),
 linear-gradient(180deg,#0f2038 0%,#2b4a6d 45%,#3f5a72 70%,#141612 100%)}
.hero-title{left:156px;top:40px;font-family:'Roboto',sans-serif;font-weight:300;color:var(--white);font-size:36px;line-height:40px}
.hero-sub{left:156px;top:80px;font-family:'Roboto',sans-serif;font-weight:300;color:#5fb7ea;font-size:26px;line-height:29px}
.hero-text{left:160px;top:151px;width:340px;color:var(--white);font-size:11.2px;line-height:12px}
.btn{display:inline-block;background:var(--blue);color:var(--white);font-size:10.5px;text-align:center;text-decoration:none}
.hero .btn{position:absolute;left:161px;top:201px;width:71px;height:22px;line-height:22px;font-size:11px}
.hero-arrow{top:158px;width:33px;height:33px;border-radius:50%;background:var(--white)}
.hero-arrow svg{display:block}

/* services */
.services{left:0;top:426px;width:894px;height:282px;background:var(--dark)}
.service{top:36px;width:150px;text-align:center}
.service h3{font-family:'Roboto',sans-serif;font-weight:400;font-size:14.5px;color:var(--white);letter-spacing:.3px;height:24px}
.service .thumb{width:148px;height:88px;margin:8px auto 0}
.service p{font-size:8.3px;line-height:11.5px;color:var(--grey-text);margin-top:15px}
.service .btn-ghost{display:inline-block;margin-top:13px;width:55px;height:16px;line-height:16px;background:var(--white);color:#222;font-size:9.5px;text-decoration:none}
.service .btn-ghost.is-active{background:var(--blue);color:var(--white)}

/* about */
.about-band{left:0;top:708px;width:894px;height:231px;background:var(--light)}
.section-title{font-family:'Roboto',sans-serif;font-weight:300;font-size:16px;color:var(--blue);letter-spacing:.2px}
.about-lead{left:112px;top:61px;width:440px;font-size:10.4px;line-height:13px;color:#111}
.about-photo{left:112px;top:96px;width:101px;height:96px}
.about-copy{left:227px;top:94px;width:330px;font-size:7.8px;line-height:11.6px;color:var(--muted)}
.about-copy p+p{margin-top:11px}
.about-band .btn{position:absolute;width:64px;height:16px;line-height:16px;font-size:10px}
.employers{left:597px;top:58px;width:186px;font-size:8px;line-height:10.6px;color:#333}
.employers p+p{margin-top:10px}

/* partners */
.partners{left:0;top:939px;width:894px;height:77px;background:var(--white)}
.partner{top:22px;height:32px;background:#e3e3e3;border-radius:3px}

/* offices */
.offices{left:0;top:1016px;width:894px;height:132px;background:var(--dark)}
.office{top:30px;width:220px;font-size:8px;line-height:11.5px;color:#e8e8e8}
.office h4{font-family:'Roboto',sans-serif;font-weight:400;font-size:12.5px;color:#5fb7ea;margin-bottom:6px}
.office p+p{margin-top:6px}
.office a{color:#5fb7ea;text-decoration:none}

/* footer */
.site-footer{left:0;top:1148px;width:894px;height:52px;background:var(--blue-band);text-align:center}
.footer-nav{display:flex;justify-content:center;gap:0;margin-top:11px}
.footer-nav a{font-size:8.5px;color:#1d2a33;text-decoration:none;padding:3px 7px}
.footer-nav a.active{background:var(--white);padding:3px 10px;margin-right:2px}
.copyright{font-size:7.8px;color:#1d2a33;margin-top:3px}
</style>
</head>
<body>

<header class="site-header">
  <div class="abs brand">
    <span class="brand-mark"></span>
    <span class="brand-name">trivexpro</span>
  </div>
  <div class="abs office-top">
    <h4>Perth Office</h4>
    Suite 4, 119 Marlow Street Subiaco Western Australia 6008<br>
    Phone: <a href="#">+61 (08) 9462 5810</a><br>
    Email: <a href="#">perth@trivexpro.com.au</a>
  </div>
  <nav class="abs main-nav">
    <a href="#" class="active">Home</a>
    <a href="#">About Us</a>
    <a href="#">Positions We Offer</a>
    <a href="#">Candidates</a>
    <a href="#">Employers</a>
    <a href="#">Contact Us</a>
  </nav>
</header>

<section class="abs hero" role="img" aria-label="Night view of an industrial power plant with cooling tower and cranes lit up">
  <h1 class="abs hero-title">Australia’s number 1</h1>
  <h2 class="abs hero-sub">Health, Safety, Environment and<br>Quality recruitment group.</h2>
  <p class="abs hero-text">TRIVEX-PRO is a Perth-based independent, specialised recruitment company with a focus on Health, Safety, Environment and Quality positions within the resources sector.</p>
  <a href="#" class="btn">Read More</a>
  <div class="abs hero-arrow" style="left:28px">
    <svg width="33" height="33" viewBox="0 0 33 33"><path d="M19 10 L12.5 16.5 L19 23" fill="none" stroke="#222" stroke-width="2.6"/></svg>
  </div>
  <div class="abs hero-arrow" style="left:833px">
    <svg width="33" height="33" viewBox="0 0 33 33"><path d="M14 10 L20.5 16.5 L14 23" fill="none" stroke="#222" stroke-width="2.6"/></svg>
  </div>
</section>

<section class="abs services">
  <div class="abs service" style="left:118px">
    <h3>HEALTH &amp; SAFETY</h3>
    <div class="thumb" role="img" aria-label="Heavy mining machinery at a coal site" style="background:linear-gradient(160deg,#5a6b7a,#3a3330 55%,#8a6a4a)"></div>
    <p>Lorem ipsum dolor sit amet, consectetur adipiscing elit. Sed id tempus enim. Etiam eros velit, Phasellus.</p>
    <a href="#" class="btn-ghost">Details</a>
  </div>
  <div class="abs service" style="left:287px">
    <h3>QUALITY</h3>
    <div class="thumb" role="img" aria-label="Miner in a hard hat holding up a mineral sample" style="background:linear-gradient(135deg,#d0a640,#6b6560 40%,#2e2a27)"></div>
    <p>Lorem ipsum dolor sit amet, consectetur adipiscing elit. Sed id tempus enim. Etiam eros velit, Phasellus.</p>
    <a href="#" class="btn-ghost is-active">Details</a>
  </div>
  <div class="abs service" style="left:456px">
    <h3>TRAINING</h3>
    <div class="thumb" role="img" aria-label="Two workers in hard hats and hi-vis gear reviewing a clipboard" style="background:linear-gradient(180deg,#6fa6dc,#d8e3ee 45%,#e08a2e 70%,#2c4f8c)"></div>
    <p>Lorem ipsum dolor sit amet, consectetur adipiscing elit. Sed id tempus enim. Etiam eros velit, Phasellus.</p>
    <a href="#" class="btn-ghost">Details</a>
  </div>
  <div class="abs service" style="left:626px">
    <h3>ENVIRONMENTAL</h3>
    <div class="thumb" role="img" aria-label="Power line pylons over a yellow canola field" style="background:linear-gradient(180deg,#c7ccd1,#aab2b6 55%,#c9c93a 75%,#8aa12a)"></div>
    <p>Lorem ipsum dolor sit amet, consectetur adipiscing elit. Sed id tempus enim. Etiam eros velit, Phasellus.</p>
    <a href="#" class="btn-ghost">Details</a>
  </div>
</section>

<section class="abs about-band">
  <h2 class="abs section-title" style="left:112px;top:34px">ABOUT US</h2>
  <p class="abs about-lead">Working from the largest database of industry professionals in Australia, TRIVEX-PRO operates exclusively in the Mining, Oil &amp; Gas, Construction and Engineering sectors.</p>
  <div class="abs about-photo" role="img" aria-label="Worker in a hard hat talking on a phone at an industrial site" style="background:linear-gradient(160deg,#c9d3dc,#5a7189 50%,#1f2a38)"></div>
  <div class="abs about-copy">
    <p>Our clients range from engineering consultancies and major owner-operator oil companies to international EPCM’s and the largest diversified mining companies in the world.</p>
    <p>In addition to providing Health, Safety, Environment and Quality professionals, we also deliver highly qualified and experienced Risk Management, Emergency Response and Training personnel.</p>
  </div>
  <a href="#" class="btn" style="left:227px;top:184px">Read More</a>

  <h2 class="abs section-title" style="left:597px;top:34px">EMPLOYERS</h2>
  <div class="abs employers">
    <p>As a specialist in sourcing Health, Safety, Environment and Quality professionals for the Mining, Oil &amp; Gas, Engineering and Construction industries, TRIVEX-PRO has a strong understanding of your requirements. Our services also extend to providing risk management, emergency response and training personnel.</p>
    <p>With access to a network of over 38,500 industry professionals throughout Australia,</p>
  </div>
  <a href="#" class="btn" style="left:598px;top:184px">Read More</a>
</section>

<section class="abs partners" aria-label="Partners and memberships">
  <svg class="abs" style="left:123px;top:32px" width="10" height="14" viewBox="0 0 10 14"><path d="M8 1 L2 7 L8 13" fill="none" stroke="#444" stroke-width="2.4"/></svg>
  <div class="abs partner" style="left:160px;width:66px"></div>
  <div class="abs partner" style="left:254px;width:80px"></div>
  <div class="abs partner" style="left:362px;width:72px"></div>
  <div class="abs partner" style="left:474px;width:116px"></div>
  <div class="abs partner" style="left:622px;width:114px"></div>
  <svg class="abs" style="left:761px;top:32px" width="10" height="14" viewBox="0 0 10 14"><path d="M2 1 L8 7 L2 13" fill="none" stroke="#444" stroke-width="2.4"/></svg>
</section>

<section class="abs offices">
  <div class="abs office" style="left:134px">
    <h4>Brisbane Office</h4>
    <p>Level 12, Harbourline Tower 208 Elm Street, Brisbane Queensland 4000</p>
    <p>Phone: <a href="#">+61 (07) 3184 6620</a><br>Email: <a href="#">brisbane@trivexpro.com.au</a></p>
  </div>
  <div class="abs office" style="left:340px">
    <h4>Hong Kong Office</h4>
    <p>22/F Lantern Plaza 41 Bayview Road<br>Wanchai, Hong Kong</p>
    <p>Phone: <a href="#">+852 3041 7756</a><br>Email: <a href="#">hongkong@trivexpro.asia</a></p>
  </div>
  <div class="abs office" style="left:541px;width:240px">
    <h4>Seoul Office</h4>
    <p>Level 18, Riverstone Tower 207 Hanbit-ro Samsung dong, Gangnam-Gu Seoul, Republic of Korea</p>
    <p>Phone: <a href="#">+82 (0) 2 5120 4318</a><br>Email: <a href="#">seoul@trivexpro.asia</a></p>
  </div>
</section>

<footer class="abs site-footer">
  <nav class="footer-nav">
    <a href="#" class="active">Home</a>
    <a href="#">About Us</a>
    <a href="#">Positions We Offer</a>
    <a href="#">Candidates</a>
    <a href="#">Employers</a>
    <a href="#">Contact Us</a>
  </nav>
  <p class="copyright">© Copyright 2013 TRIVEX-PRO. All Rights Reserved.</p>
</footer>

</body>
</html>
```